Oil and gas industry project solutions company needs professional cards with Canadian aboriginal fee

We are a aboriginally owned company that is focused on Project Planning, Management, Inspection & Consulting for Canada's Petroleum Industry. We have a logo that we would like to incorporate into a professional looking business card. We are professionals that offer services from project inception to completion.

Target Market(s)

Major industry leaders like NorthRidge Pipelines, Vantor, Kelstrand Energy, Brimwell etc.

Industry/Entity Type

Industry

Contact Information for Business Card

Reid Forbin
reid@kolbymarsh.ca
250 418 9067

Requirements
Must have
• KolbyMarsh Inc. logo.
• Address is: RR4, Site2, Comp7 Fort St. John, BC V1J 8K3 Traditional Territory of the Treaty 8 People
• Colors that are in logo
• Banner or picture on back
• Ability to put different names and contacts
• Website: kolbymarsh.ca
• "Project Planning, Management, Inspection & Consulting for Canada's Petroleum Industry"

```html
<!DOCTYPE html>
<html lang="en">
<head>
<meta charset="utf-8">
<title>KolbyMarsh Inc. — Business Card</title>
<link rel="stylesheet" href="https://fonts.googleapis.com/css2?family=Open+Sans:wght@400;600;700&display=swap">
<style>
  :root {
    --canvas: #ecebe8;
    --navy: #262b6b;
    --panel-light: #e9e8eb;
    --panel-mid: #c9ccd6;
    --leaf-green: #6cb043;
    --white: #ffffff;
    --text-soft: #e6e7f2;
  }
  * { box-sizing: border-box; margin: 0; padding: 0; }
  html, body {
    width: 1200px; height: 900px; overflow: hidden;
    background: var(--canvas);
    font-family: "Open Sans", Arial, sans-serif;
  }
  .business-card {
    position: absolute; left: 160px; top: 178px;
    width: 880px; height: 544px;
    background: var(--navy);
    overflow: hidden;
    box-shadow: 0 18px 40px rgba(0,0,0,0.18);
  }
  .symbol-area {
    position: absolute; left: 560px; top: 0;
    width: 320px; height: 544px;
    background: linear-gradient(90deg, rgba(38,43,107,0) 0%, var(--panel-mid) 38%, var(--panel-light) 100%);
  }
  .symbol-area::after {
    content: ""; position: absolute; right: 0; bottom: 0;
    width: 230px; height: 200px;
    background: linear-gradient(160deg, rgba(108,176,67,0) 0%, rgba(108,176,67,0.55) 100%);
  }
  .company-name {
    position: absolute; left: 46px; top: 70px;
    color: var(--white);
    font-size: 40px; font-weight: 700; letter-spacing: -0.5px;
    line-height: 1;
  }
  .person-name {
    position: absolute; left: 46px; top: 196px;
    color: var(--white);
    font-size: 33px; font-weight: 600;
  }
  .address {
    position: absolute; left: 46px; top: 278px;
    color: var(--text-soft);
    font-size: 22px; line-height: 33px;
  }
  .contact-list {
    position: absolute; left: 46px; top: 386px;
    list-style: none;
    color: var(--text-soft);
    font-size: 22px;
  }
  .contact-list li {
    display: flex; align-items: center; gap: 18px;
    height: 37.5px;
  }
  .contact-icon { width: 17px; height: 17px; fill: var(--white); flex: none; }
</style>
</head>
<body>
  <main class="business-card">
    <div class="symbol-area" role="img" aria-label="Company symbol: stylised droplet with feather and leaf in grey, blue and green"></div>

    <div class="company-name">KolbyMarsh Inc.</div>
    <h1 class="person-name">Reid Forbin</h1>
    <p class="address">RR4, Site2, Comp7 Fort<br>St. John, BC V1J 8K3</p>

    <ul class="contact-list">
      <li>
        <svg class="contact-icon" viewBox="0 0 24 24" aria-hidden="true"><path d="M6.6 10.8c1.4 2.8 3.8 5.1 6.6 6.6l2.2-2.2c.3-.3.7-.4 1-.2 1.1.4 2.3.6 3.6.6.6 0 1 .4 1 1V20c0 .6-.4 1-1 1C10.6 21 3 13.4 3 4c0-.6.4-1 1-1h3.5c.6 0 1 .4 1 1 0 1.3.2 2.5.6 3.6.1.3 0 .7-.2 1L6.6 10.8z"/></svg>
        <span>250 418 9067</span>
      </li>
      <li>
        <svg class="contact-icon" viewBox="0 0 24 24" aria-hidden="true"><path d="M2 5h20v14H2z M2 5l10 8 10-8" fill="none" stroke="#fff" stroke-width="0"/><path d="M2 5h20v2l-10 7L2 7z"/><path d="M2 9l10 7 10-7v10H2z"/></svg>
        <span>reid@kolbymarsh.ca</span>
      </li>
      <li>
        <svg class="contact-icon" viewBox="0 0 24 24" aria-hidden="true"><circle cx="12" cy="12" r="10"/><path d="M12 2c-3 3-3 17 0 20M12 2c3 3 3 17 0 20M2 12h20M4 7h16M4 17h16" fill="none" stroke="#262b6b" stroke-width="1.4"/></svg>
        <span>www.kolbymarsh.ca</span>
      </li>
    </ul>
  </main>
</body>
</html>
```